fix and make current flyer more professorial looking

we have the attached flyer that we want to be reworked. Feel free to completely redo it but we do like the main image about where it is. here are some other thoughts.

Too much space for Korvo Logo
Real Competitive should be a different color
Bullets I want in their own callout section, better than it is there now
Logos should be closer to the bottom in a line and not at big

Highlight speed cost and support

```html
<!DOCTYPE html>
<html lang="en">
<head>
<meta charset="utf-8">
<title>Korvo — Real Competitive Advantages</title>
<link href="https://fonts.googleapis.com/css2?family=Roboto:wght@300;400;500;700;900&display=swap" rel="stylesheet">
<style>
  :root {
    --blue: #4558a8;
    --heading-blue: #1f3f8f;
    --cyan: #00a6cf;
    --ink: #231f20;
    --panel: #2f2a2b;
    --grey: #d6d7d9;
    --muted: #4a4a4a;
    --white: #ffffff;
    --text: #1e1e1e;
  }
  html, body { margin: 0; padding: 0; overflow: hidden; background: var(--white); }
  .flyer {
    position: relative; width: 927px; height: 1200px; overflow: hidden;
    font-family: "Roboto", Arial, sans-serif; color: var(--text); background: var(--white);
  }
  .block { position: absolute; }

  /* hero */
  .hero-photo-left { left: 0; top: 0; width: 463px; height: 339px;
    background: linear-gradient(160deg, #3f4f9a 0%, #2e3b7c 45%, #4a5ba6 100%); }
  .hero-photo-right { left: 463px; top: 0; width: 378px; height: 339px;
    background: linear-gradient(200deg, #dcdcdc 0%, #8f8f8f 45%, #4a4a4a 80%, #7a7a7a 100%); }
  .accent-vertical { left: 878px; top: 80px; width: 49px; height: 344px; background: var(--blue); }
  .accent-band { left: 463px; top: 374px; width: 464px; height: 50px; background: var(--blue); }

  .brand-name { left: 56px; top: 118px; margin: 0; font-size: 64px; font-weight: 300;
    letter-spacing: 6px; color: var(--white); line-height: 1; }
  .tagline { left: 56px; top: 226px; margin: 0; color: var(--white); font-size: 21px; line-height: 27px; }
  .tagline strong { display: block; font-weight: 700; color: var(--cyan); letter-spacing: 0.3px; }
  .tagline span { display: block; font-weight: 400; letter-spacing: 1.6px; }

  /* sections */
  .section-title { margin: 0; font-size: 31px; font-weight: 900; color: var(--ink); line-height: 1; }
  .section-title em { font-style: normal; color: var(--heading-blue); }
  .section-copy { margin: 0; font-size: 17.6px; font-weight: 300; line-height: 21.8px; }
  .section-copy strong { font-weight: 700; color: var(--heading-blue); }

  .what-we-do { left: 56px; top: 409px; width: 345px; }
  .what-we-do .section-copy { margin-top: 29px; }

  .apps-panel { left: 463px; top: 424px; width: 464px; height: 330px; background: var(--ink); color: var(--white); }
  .apps-callout { position: absolute; left: 30px; top: 26px; width: 384px; height: 276px;
    background: var(--panel); border-left: 5px solid var(--cyan); box-sizing: border-box; padding: 18px 0 0 22px; }
  .apps-callout h3 { margin: 0; font-size: 15.5px; font-weight: 700; line-height: 20px; color: var(--cyan); }
  .apps-list { margin: 14px 0 0; padding: 0; list-style: none;
    font-size: 15.5px; font-weight: 400; line-height: 21.8px; }
  .apps-list li { position: relative; padding-left: 22px; }
  .apps-list li::before { content: ""; position: absolute; left: 2px; top: 6px; width: 9px; height: 5px;
    border-left: 2px solid var(--cyan); border-bottom: 2px solid var(--cyan); transform: rotate(-45deg); }

  .about-band { left: 0; top: 754px; width: 927px; height: 376px; background: var(--grey); }
  .cyan-band { left: 463px; top: 754px; width: 464px; height: 48px; background: var(--cyan); }
  .chip-photo { left: 463px; top: 802px; width: 407px; height: 276px;
    background: radial-gradient(ellipse at 50% 60%, #f2f2f2 0%, #8a8a8a 18%, #2a2a2a 48%, #0c0c0c 100%); }
  .blue-base { left: 0; top: 1078px; width: 463px; height: 52px; background: var(--blue); }

  .about-us { left: 56px; top: 792px; width: 355px; }
  .about-us .section-copy { margin-top: 29px; }

  .partners { left: 56px; top: 1046px; width: 380px; display: flex; align-items: center; justify-content: space-between;
    font-size: 13px; font-weight: 500; letter-spacing: 1.2px; text-transform: uppercase; color: var(--muted); }
  .partner { display: flex; align-items: center; gap: 5px; }
  .partner .dot { width: 10px; height: 10px; border-radius: 50%; background: var(--muted); }

  /* footer */
  .footer { left: 0; top: 1130px; width: 927px; height: 70px; background: var(--ink); color: var(--white); font-size: 17px; }
  .contact { position: absolute; display: flex; align-items: center; gap: 10px; top: 23px; }
  .contact svg { width: 18px; height: 18px; fill: var(--white); }
  .contact-phone { left: 57px; font-weight: 700; letter-spacing: 2.5px; }
  .contact-mail { left: 320px; }
  .contact-web { left: 631px; }
</style>
</head>
<body>
<main class="flyer">
  <div class="block hero-photo-left" role="img" aria-label="Blue-tinted close-up photo of a circuit board"></div>
  <div class="block hero-photo-right" role="img" aria-label="Black and white close-up photo of server hardware with heat sinks"></div>
  <div class="block accent-vertical"></div>
  <div class="block accent-band"></div>

  <h1 class="block brand-name">KORVO</h1>
  <p class="block tagline"><strong>REAL COMPETITIVE ADVANTAGES</strong><span>IN MEDIA AND ENTERTAINMENT</span></p>

  <section class="block what-we-do">
    <h2 class="section-title"><em>WHAT</em> WE DO</h2>
    <p class="section-copy">When it comes to competitive advantages, it doesn't get much better than being able to <strong>cut delivery time by 80%</strong>, <strong>decrease cost by up to 30%</strong> from traditional distribution outlets, and provide a <strong>plug-and play solution</strong> with a variety of different manufacturer's components. KORVO has spent the last 10 years navigating the media and entertainment landscape to be able to provide you with the most current, reliable platform to optimize the user experience.</p>
  </section>

  <aside class="block apps-panel">
    <div class="apps-callout">
      <h3>OUR DIGITAL MEDIA PLATFORMS ARE IDEAL<br>FOR FOLLOWING TYPES OF APPLICATIONS</h3>
      <ul class="apps-list">
        <li>MEDIA RETENTION</li>
        <li>VIDEO TRANSPORT</li>
        <li>VIDEO CONTENT MANAGMENT</li>
        <li>VIDEO ENCODING/DECODING</li>
        <li>VIDEO STREAM RECORDING</li>
        <li>ON-DEMAND MEDIA</li>
        <li>DIGITAL ARCHIVE &amp; RETRIEVAL</li>
        <li>COLLABORATIVE VIDEO CONFERENCING</li>
        <li>WEBCASTING</li>
      </ul>
    </div>
  </aside>

  <div class="block about-band"></div>
  <div class="block cyan-band"></div>
  <div class="block chip-photo" role="img" aria-label="Glowing processor chip on a dark circuit board"></div>
  <div class="block blue-base"></div>

  <section class="block about-us">
    <h2 class="section-title"><em>ABOUT</em> US</h2>
    <p class="section-copy">With over 50 years of combined expertise in the sourcing, configuring and delivering of customized business solutions, Korvo Distributing is commited to providing its parters with impactfull, timelles alternatives that drive profit to the bottom line.</p>
  </section>

  <div class="block partners">
    <span class="partner">Stratos</span>
    <span class="partner">Halden Media</span>
    <span class="partner">Vireo</span>
    <span class="partner"><span class="dot"></span>Qbn</span>
  </div>

  <footer class="block footer">
    <span class="contact contact-phone">
      <svg viewBox="0 0 24 24"><path d="M6.6 10.8a15.1 15.1 0 0 0 6.6 6.6l2.2-2.2a1 1 0 0 1 1-.25 11.4 11.4 0 0 0 3.6.57 1 1 0 0 1 1 1V20a1 1 0 0 1-1 1A17 17 0 0 1 3 4a1 1 0 0 1 1-1h3.5a1 1 0 0 1 1 1c0 1.25.2 2.45.57 3.57a1 1 0 0 1-.25 1z"/></svg>
      (555) 218-4406
    </span>
    <span class="contact contact-mail">
      <svg viewBox="0 0 24 24"><path d="M2 9l10-6 10 6v12H2zm2 1.2V19h16v-8.8l-8 5z"/></svg>
      info@korvodistributing.com
    </span>
    <span class="contact contact-web">
      <svg viewBox="0 0 24 24"><path d="M12 2a10 10 0 1 0 0 20 10 10 0 0 0 0-20zm6.9 6h-2.9a15.7 15.7 0 0 0-1.4-3.6A8 8 0 0 1 18.9 8zM12 4c.8 1.2 1.5 2.5 1.9 4h-3.8c.4-1.5 1.1-2.8 1.9-4zM4.3 14a8 8 0 0 1 0-4h3.4a16 16 0 0 0 0 4zm.8 2h2.9c.3 1.3.8 2.5 1.4 3.6A8 8 0 0 1 5.1 16zM8 8H5.1a8 8 0 0 1 4.3-3.6C8.8 5.5 8.3 6.7 8 8zm4 12c-.8-1.2-1.5-2.5-1.9-4h3.8c-.4 1.5-1.1 2.8-1.9 4zm2.3-6H9.7a14 14 0 0 1 0-4h4.6a14 14 0 0 1 0 4zm.3 5.6c.6-1.1 1.1-2.3 1.4-3.6h2.9a8 8 0 0 1-4.3 3.6zm1.7-5.6a16 16 0 0 0 0-4h3.4a8 8 0 0 1 0 4z"/></svg>
      www.korvodistributing.com
    </span>
  </footer>
</main>
</body>
</html>
```